Business Card needed for Drainor, a growing Septic Service company

Drainor, a growing local septic service company in Pennsylvania, needs updated business cards. We'd like the business card to feature our logo and communicate that we provide Septic Pumping, Installations/Repairs, Restroom Rentals, and 24/7 Emergency Service. The business card should be eye-catching, bold, and clean/simple. We have been in business almost 10 years and would like to expand and update our business brand and image.

Target Market(s)

Residential and Commercial, New and Current Homeowners

Industry/Entity Type

Service

Contact Information for Business Card

Contact on the business card should be: Dean Harlow Owner & Operator
Phone: 555-555-0187
Email: service@drainor-example.com
Website: www.drainor-example.com
Address: 812 Millbrook Lane Cedar Glen ST 00000

Font styles to use
Sans Serif

Colors

Designer to choose colors to be used in the design.

Requirements
Must have
• Feature logo on both side of business card.
Nice to have
• We envision the contact information on one side and our services listed on the other side. Utilize the green from the symbol in our logo as part of the design, overall design color scheme should be white, grey, black.

```html
<!DOCTYPE html>
<html lang="en">
<head>
<meta charset="utf-8">
<title>Drainor Business Card</title>
<link rel="stylesheet" href="https://fonts.googleapis.com/css2?family=Lato:wght@400;700;900&family=Roboto:wght@400&display=swap">
<style>
  :root {
    --page-bg: #d9d9d9;
    --card-bg: #ededed;
    --ink: #111111;
    --text: #1e1e1e;
    --green: #7cb83e;
  }
  * { margin: 0; padding: 0; box-sizing: border-box; }
  html, body {
    width: 1200px; height: 820px; overflow: hidden;
    background: var(--page-bg);
  }
  .canvas { position: relative; width: 1200px; height: 820px; }
  .card {
    position: absolute; top: 128px;
    width: 322px; height: 565px;
    background: var(--card-bg);
  }
  .card--front { left: 242px; text-align: center; }
  .card--back { left: 636px; }

  /* Front */
  .brand-mark {
    position: absolute; left: 131px; top: 88px;
    width: 60px; height: 60px; background: var(--green);
  }
  .brand-name {
    position: absolute; left: 0; right: 0; top: 158px;
    font: 900 32px/1 "Lato", sans-serif;
    letter-spacing: 1px; color: var(--ink);
  }
  .person-name {
    position: absolute; left: 0; right: 0; top: 243px;
    font: 900 26px/1 "Lato", sans-serif; color: var(--ink);
  }
  .person-title {
    position: absolute; left: 0; right: 0; top: 273px;
    font: 400 17px/1 "Lato", sans-serif; color: var(--green);
  }
  .contact-icons {
    position: absolute; left: 0; right: 0; top: 318px;
    display: flex; justify-content: center; gap: 12px;
  }
  .contact-icons svg { width: 17px; height: 17px; }
  .contact-line {
    position: absolute; left: 0; right: 0;
    font: 400 15px/1 "Roboto", sans-serif;
    letter-spacing: 1.3px; color: var(--text);
  }
  .contact-line--phone { top: 355px; }
  .contact-line--email { top: 380px; font-size: 14px; letter-spacing: 0.8px; }
  .contact-line--web { top: 414px; font-size: 14px; letter-spacing: 0.8px; }
  .address-divider {
    position: absolute; left: 0; right: 0; top: 452px;
    display: flex; justify-content: center; align-items: center; gap: 10px;
  }
  .address-divider .rule { width: 20px; height: 2px; background: var(--green); }
  .address-divider svg { width: 18px; height: 18px; }
  .address {
    position: absolute; left: 0; right: 0; top: 490px;
    font: 400 15px/20px "Roboto", sans-serif;
    letter-spacing: 1.3px; color: var(--text);
  }

  /* Back */
  .back-brand {
    position: absolute; left: 48px; top: 186px;
    display: flex; align-items: center; gap: 14px;
  }
  .back-brand .mark { width: 40px; height: 40px; background: var(--green); }
  .back-brand .name {
    font: 900 38px/1 "Lato", sans-serif;
    letter-spacing: 1px; color: var(--ink);
  }
  .service-list { position: absolute; left: 52px; top: 272px; list-style: none; }
  .service-list li {
    display: flex; align-items: center; gap: 11px;
    height: 20px; margin-bottom: 18.7px;
    font: 700 15.5px/1 "Lato", sans-serif; color: var(--ink);
  }
  .service-list li::before {
    content: ""; width: 14px; height: 14px;
    background: var(--green); flex: none;
  }
</style>
</head>
<body>
<div class="canvas">

  <section class="card card--front">
    <div class="brand-mark"></div>
    <div class="brand-name">DRAINOR</div>
    <h1 class="person-name">DEAN HARLOW</h1>
    <p class="person-title">Owner &amp; Operator</p>

    <div class="contact-icons">
      <svg viewBox="0 0 20 20" aria-label="Phone">
        <circle cx="10" cy="10" r="9" fill="none" stroke="#7cb83e" stroke-width="1.2"/>
        <path d="M6.5 5.5l2 0 .8 2.2-1.2 1a6 6 0 0 0 3.2 3.2l1-1.2 2.2.8v2c-4.5.4-8.4-3.5-8-8z" fill="#7cb83e"/>
      </svg>
      <svg viewBox="0 0 20 20" aria-label="Website">
        <circle cx="10" cy="10" r="9" fill="none" stroke="#7cb83e" stroke-width="1.2"/>
        <circle cx="10" cy="10" r="5" fill="none" stroke="#7cb83e" stroke-width="1.2"/>
        <path d="M7 7.5c1.5 0 2 1 1.6 2.2-.4 1 .4 2 1.4 2.3M11.5 5.5c-.3 1 .5 1.7 1.5 1.8" fill="none" stroke="#7cb83e" stroke-width="1.1"/>
      </svg>
      <svg viewBox="0 0 20 20" aria-label="Email">
        <circle cx="10" cy="10" r="9" fill="none" stroke="#7cb83e" stroke-width="1.2"/>
        <rect x="5" y="6.8" width="10" height="6.6" fill="#7cb83e"/>
        <path d="M5.3 7.2L10 10.8l4.7-3.6" fill="none" stroke="#ededed" stroke-width="0.9"/>
      </svg>
    </div>

    <p class="contact-line contact-line--phone">555-555-0187</p>
    <p class="contact-line contact-line--email">service@drainor-example.com</p>
    <p class="contact-line contact-line--web">www.drainor-example.com</p>

    <div class="address-divider">
      <span class="rule"></span>
      <svg viewBox="0 0 20 20" aria-label="Address">
        <circle cx="10" cy="10" r="9" fill="none" stroke="#7cb83e" stroke-width="1.2"/>
        <path d="M10 15.5s-3.2-3.6-3.2-6.2a3.2 3.2 0 0 1 6.4 0c0 2.6-3.2 6.2-3.2 6.2z" fill="#7cb83e"/>
        <circle cx="10" cy="9.2" r="1.2" fill="#ededed"/>
      </svg>
      <span class="rule"></span>
    </div>

    <p class="address">812 Millbrook Lane<br>Cedar Glen ST 00000</p>
  </section>

  <section class="card card--back">
    <div class="back-brand">
      <span class="mark"></span>
      <span class="name">DRAINOR</span>
    </div>
    <ul class="service-list">
      <li>SEPTIC PUMPING</li>
      <li>INSTALLATIONS/REPAIRS</li>
      <li>RESTROOM RENTALS</li>
      <li>24/7 EMERGENCY SERVICE</li>
    </ul>
  </section>

</div>
</body>
</html>
```